Modern Spot UV Business Card design

We are a relatively new real estate agency. We need a business card that reflects the professionalism and prestige of our company but is also modern and fresh, based around our logo.
We would love to utilise spot UV.
Happy to let the designers use their imagination and see what they come up with (we're not very creative, so have no ideas for you, sorry) :-)
We'd like one for each staff member, but I've just provided one staff members photo here to avoid confusion.

Target Market(s)

Families

Industry/Entity Type

Real Estate Agent

Contact Information for Business Card

Colin Varga - Director & Principal
Mobile: 0491 527 806
Email: colin.varga@vbrokers.example.com.au
Phone: (08) 7364 9150
Fax: (08) 7364 9182
www.vargabrokersrealestate.example.com.au

Font styles to use
Other font styles liked:
• Kabel Dm BT

Requirements
Must have
• Contact details, logo, photo, spot UV
Nice to have
• Modern interesting features that will make people comment. Nothing too feminine nor too masculine.
Should not have
• No houses! Nothing typical of a real estate agent.

```html
<!DOCTYPE html>
<html lang="en">
<head>
<meta charset="utf-8">
<title>Varga Brokers Real Estate – Business Card</title>
<link href="https://fonts.googleapis.com/css2?family=Didact+Gothic&family=Open+Sans:wght@400;700&display=swap" rel="stylesheet">
<style>
  :root {
    --page: #e9e9e9;
    --card-dark: #4f4f4f;
    --card-light: #7b7b7b;
    --cyan: #7fe3f7;
    --blue: #3aa9f2;
    --white: #ffffff;
    --photo-light: #f4f4f4;
    --photo-mid: #8d8a88;
  }
  * { box-sizing: border-box; margin: 0; padding: 0; }
  html, body { width: 1200px; height: 1200px; overflow: hidden; background: var(--page); }
  .canvas {
    width: 1200px; height: 1200px;
    display: flex; flex-direction: column; align-items: center; justify-content: center; gap: 50px;
  }
  .card {
    position: relative; width: 880px; height: 500px; overflow: hidden;
    background: linear-gradient(160deg, var(--card-light) 0%, var(--card-dark) 75%);
    box-shadow: 0 10px 30px rgba(0,0,0,.25);
  }
  .card-shapes { position: absolute; inset: 0; }
  .brand {
    position: absolute; left: 70px; top: 150px;
    font-family: "Didact Gothic", sans-serif; color: var(--white);
  }
  .brand-name { font-size: 86px; line-height: 1; letter-spacing: -1px; }
  .brand-row { display: flex; align-items: center; gap: 26px; margin-top: 6px; }
  .brand-sub { font-size: 60px; line-height: 1; }
  .tagline {
    border-left: 2px solid rgba(255,255,255,.7); padding-left: 16px;
    font-size: 28px; line-height: 1.05; color: var(--white); letter-spacing: 1px;
  }
  .contact {
    position: absolute; right: 36px; top: 40px; text-align: right;
    font-family: "Open Sans", sans-serif; color: var(--white);
  }
  .contact-name { font-size: 30px; font-weight: 700; line-height: 1.1; }
  .contact-title { font-size: 19px; margin-bottom: 24px; }
  .contact-line { font-size: 19px; line-height: 1.8; white-space: nowrap; }
  .contact-web { font-size: 16px; line-height: 1.9; }
  .contact-gap { margin-top: 18px; }
</style>
</head>
<body>
<main class="canvas">

  <section class="card card-front" aria-label="Card front">
    <svg class="card-shapes" viewBox="0 0 880 500" width="880" height="500" aria-hidden="true">
      <polygon points="745,0 880,0 880,215" fill="var(--white)"/>
      <polygon points="700,0 745,0 880,215 880,285" fill="var(--cyan)"/>
      <polygon points="880,320 880,370 650,500 560,500" fill="var(--cyan)"/>
      <polygon points="0,462 620,462 560,500 0,500" fill="var(--blue)"/>
    </svg>
    <div class="brand">
      <div class="brand-name">Varga Brokers</div>
      <div class="brand-row">
        <span class="brand-sub">Real Estate</span>
        <span class="tagline">Helping you make<br>your next move</span>
      </div>
    </div>
  </section>

  <section class="card card-back" aria-label="Card back">
    <svg class="card-shapes" viewBox="0 0 880 500" width="880" height="500" aria-hidden="true">
      <polygon points="0,20 360,20 440,120 440,390 370,440 0,440" fill="var(--cyan)"/>
      <polygon points="0,56 345,56 408,136 408,372 355,404 0,404" fill="var(--photo-light)"/>
      <polygon points="0,455 480,455 480,500 0,500" fill="var(--cyan)"/>
      <polygon points="500,430 880,430 880,500 500,500" fill="var(--blue)"/>
      <polygon points="500,430 540,430 540,500 500,500" fill="var(--cyan)"/>
    </svg>
    <svg class="card-shapes" viewBox="0 0 880 500" width="880" height="500" role="img" aria-label="Portrait photo of Colin Varga in a grey suit">
      <defs>
        <radialGradient id="portraitTone" cx="50%" cy="55%" r="50%">
          <stop offset="0%" stop-color="var(--photo-mid)" stop-opacity=".55"/>
          <stop offset="100%" stop-color="var(--photo-light)" stop-opacity="0"/>
        </radialGradient>
      </defs>
      <polygon points="0,56 345,56 408,136 408,372 355,404 0,404" fill="url(#portraitTone)"/>
    </svg>
    <div class="contact">
      <div class="contact-name">Colin Varga</div>
      <div class="contact-title">Director &amp; Principal</div>
      <div class="contact-line">Mobile: 0491 527 806</div>
      <div class="contact-line">Phone: (08) 7364 9150</div>
      <div class="contact-line">Fax: (08) 7364 9182</div>
      <div class="contact-line contact-web contact-gap">Email: colin.varga@vbrokers.example.com.au</div>
      <div class="contact-line contact-web">www.vargabrokersrealestate.example.com.au</div>
    </div>
  </section>

</main>
</body>
</html>
```